依頼詳細
【外貨両替】
外貨両替は学校へ出向いて行う、出張両替とご自宅へ外貨をお届けする外貨宅配の2プランがございます。どちらのプランにするかは学校の意向や参加者の規模や要望によります。

【フェリシオンクレスト】
外貨両替(現金)以外のお金としてトラベルマネーカード(フェリシオンクレスト)の紹介をしております。こちらはキャッシュレスに対応したカードで使い方はクレジットカードと同じですが、チャージした金額の範囲でご利用頂けるカードです。

今回、制作するパンフレットは旅行会社から旅行参加者へ配布してご質問等があれば旅行会社ではなく直接当社が窓口となり、旅行参加者からの質問等を受付いたします。
今回制作するパンフレットとは別に両替の申込書面、フェリシオンクレストの申込書面は別となります。あくまでも全体の案内、問い合わせ先の案内をするパンフレットです。
記載項目
資料を添付致しますので、要点をまとめてA4サイズカラー裏表で制作をお願い致します。
サイズ
A4
ページ数
両面
希望イメージ
シンプル 複雑
単色 カラフル
暗い 明るい
日常 高級
遊び心 厳粛
未来的 伝統的
女性的 男性的
希望する色
赤系、青系
納品ファイル
• イラストレーター形式 (.ai)
補足説明
■ 選んだ理由

社内で選考した結果、一番わかりやすく好評であった為当選とさせていただきました。

■ 提案者全員のお礼・コメント

この度は短期間でしたが、沢山の方にご参加頂き、またどの提案も良いものばかりでした。
また次回依頼する場合も宜しくお願い致します。

```html
<!DOCTYPE html>
<html lang="ja">
<head>
<meta charset="utf-8">
<title>スムーズな旅行には事前両替が安心です！</title>
<link rel="stylesheet" href="https://fonts.googleapis.com/css2?family=Noto+Sans+JP:wght@400;500;700;900&family=Roboto:wght@400;700&display=swap">
<style>
  :root{
    --red:#d7141e;
    --ink:#1b1b1f;
    --navy:#1d2f5c;
    --paper:#ffffff;
    --band:#eef0f3;
    --band-dark:#e3e6ea;
    --globe-a:#dfe6ee;
    --globe-b:#b8c4d2;
    --cart-a:#c9a64a;
    --cart-b:#6f8a3a;
    --hands-a:#f3d2b5;
    --hands-b:#e48a3a;
  }
  *{margin:0;padding:0;box-sizing:border-box}
  html,body{width:846px;height:1200px;overflow:hidden;background:var(--paper)}
  body{font-family:"Noto Sans JP",sans-serif;color:var(--ink);position:relative}

  .backdrop{position:absolute;inset:0;width:846px;height:1200px}

  .brand{position:absolute;top:22px;right:30px;display:flex;align-items:center;gap:8px;
    font-size:17px;font-weight:500;color:var(--navy)}
  .brand-dot{width:16px;height:16px;border-radius:50%;background:var(--red)}

  .headline{position:absolute;left:36px;top:48px}
  .headline-lead{font-size:50px;font-weight:900;letter-spacing:1px;line-height:1.1}
  .headline-main{font-size:78px;font-weight:900;letter-spacing:2px;line-height:1.2;margin-top:4px}
  .headline-main .accent{color:var(--red)}

  .intro{position:absolute;left:36px;top:232px;font-size:13.5px;font-weight:500;line-height:1.65;color:#333;z-index:2}

  .globe-art{position:absolute;left:470px;top:225px;width:360px;height:255px;border-radius:50% 50% 30% 30%;
    background:radial-gradient(ellipse at 50% 40%,var(--globe-a),var(--globe-b) 75%,transparent 76%)}

  .service-label{font-family:"Roboto",sans-serif;font-weight:700;font-size:30px;color:#c4c9d0;letter-spacing:1px;line-height:1.2}
  .service-lead{font-size:31px;font-weight:900;line-height:1.3}
  .service-name{font-size:36px;font-weight:900;color:var(--red);line-height:1.3}

  .service-one{position:absolute;left:440px;top:500px;z-index:2}
  .service-two{position:absolute;left:36px;top:805px;z-index:2}

  .cart-art{position:absolute;left:20px;top:575px;width:380px;height:210px;border-radius:14px;
    background:linear-gradient(135deg,var(--cart-a),var(--cart-b))}
  .hands-art{position:absolute;left:470px;top:920px;width:360px;height:270px;border-radius:16px;
    background:linear-gradient(160deg,var(--hands-a),var(--hands-b))}

  .points{list-style:none;font-size:14px;font-weight:700;line-height:1.75;z-index:2}
  .points li{position:relative;padding-left:14px}
  .points li::before{content:"";position:absolute;left:0;top:9px;width:7px;height:7px;border-radius:50%;background:var(--red)}
  .points .note{font-size:11px;font-weight:500}
  .points-one{position:absolute;left:470px;top:640px}
  .points-two{position:absolute;left:36px;top:950px}
</style>
</head>
<body>
  <svg class="backdrop" viewBox="0 0 846 1200" aria-hidden="true">
    <polygon points="0,520 846,430 846,820 0,900" fill="var(--band)"/>
    <polygon points="0,900 846,820 846,860 0,960" fill="var(--band-dark)"/>
    <polygon points="0,960 846,860 846,1200 0,1200" fill="#f7f8fa"/>
  </svg>

  <div class="brand"><span class="brand-dot"></span>Voyage Bridge</div>

  <header class="headline">
    <h1 class="headline-lead">スムーズな旅行には</h1>
    <p class="headline-main"><span class="accent">事前両替</span>が安心です！</p>
  </header>

  <div class="globe-art" role="img" aria-label="地球儀と飛行機、トラベルマネーカードのイラスト"></div>

  <p class="intro">
    旅行先では両替ができる場所が限られています。<br>
    特にアフターコロナの現在、市中の外貨両替窓口が激減！<br>
    海外旅行先で安心して楽しんでいただけるよう、<br>
    外貨は一括して事前に準備することをオススメします。
  </p>

  <section class="service-one">
    <p class="service-label">SERVICE 1</p>
    <h2 class="service-lead">学校へ出向いて行う</h2>
    <p class="service-name">《出張両替》</p>
  </section>

  <div class="cart-art" role="img" aria-label="台車で運ばれる紙幣の束と硬貨のイラスト"></div>

  <ul class="points points-one">
    <li>最大32通貨の両替が可能！</li>
    <li>小額紙幣が中心で使い勝手抜群！</li>
    <li>お得な優遇レートを適用致します！<span class="note">※適用条件あり</span></li>
    <li>全国の学校へ無料出張致します！</li>
    <li>帰国後に余った紙幣は優遇レートで日本円へ！</li>
  </ul>

  <section class="service-two">
    <p class="service-label">SERVICE 2</p>
    <h2 class="service-lead">自宅へ外貨をお届けする</h2>
    <p class="service-name">《外貨宅配》</p>
  </section>

  <ul class="points points-two">
    <li>*17通貨の両替が可能！</li>
    <li>小額紙幣が中心で使い勝手抜群！</li>
    <li>旅行前にご自宅へ外貨をお届け！</li>
    <li>送料は全額当社負担で全国無料！</li>
    <li>帰国後に余った紙幣は優遇レートで日本円へ！</li>
  </ul>

  <div class="hands-art" role="img" aria-label="外貨の入った箱を手渡しで届けるイラスト"></div>
</body>
</html>
```